Book cover design for the book titled "Quieter Under Lanterns."

create a book cover. The book title is, "Quieter Under Lanterns: A Ledger of Harbour Songs Across Mild Winters." The purpose of the book is to create awareness of how childhood trauma is impacting 7 out of 10 adults in the world today and that two-thirds of children will experience neglect and or abuse before their 18th birthday. One victim described that his mental and physical illness resulting from childhood trauma felt like he wa being pulled to the ground, that the force was "quieter under lanterns." The design should be clean and simple and communicate a crisis.

```html
<!DOCTYPE html>
<html lang="en">
<head>
<meta charset="utf-8">
<title>Quieter Under Lanterns — Book Cover</title>
<link rel="stylesheet" href="https://fonts.googleapis.com/css2?family=Oswald:wght@400;600;700&family=Fira+Sans:wght@700;800&display=swap">
<style>
  :root {
    --backdrop: #e4e4e4;
    --paper: #f2f2f2;
    --crisis-red: #e32227;
    --ink: #0c0b0c;
    --white: #ffffff;
  }
  html, body {
    margin: 0;
    padding: 0;
    width: 1200px;
    height: 900px;
    overflow: hidden;
    background: var(--backdrop);
  }
  .stage {
    width: 1200px;
    height: 900px;
    display: flex;
    align-items: center;
    justify-content: center;
  }
  .book-cover {
    width: 611px;
    height: 860px;
    background: var(--paper);
    display: block;
  }
  .title-word {
    font-family: "Oswald", "Arial Narrow", sans-serif;
    font-weight: 700;
    fill: var(--crisis-red);
  }
  .title-connector {
    font-family: "Oswald", "Arial Narrow", sans-serif;
    font-weight: 400;
    fill: var(--crisis-red);
  }
  .pull-gap {
    fill: var(--paper);
  }
  .author-name {
    font-family: "Fira Sans", Arial, sans-serif;
    font-weight: 700;
    fill: var(--white);
  }
  .subtitle {
    font-family: "Fira Sans", Arial, sans-serif;
    font-weight: 800;
    fill: var(--ink);
    letter-spacing: 3.2px;
  }
</style>
</head>
<body>
<main class="stage">
  <svg class="book-cover" viewBox="0 0 611 860" xmlns="http://www.w3.org/2000/svg" role="img"
       aria-label="Book cover: Quieter Under Lanterns — A Ledger of Harbour Songs Across Mild Winters, by Jane Doe">
    <defs>
      <linearGradient id="pull-gradient" x1="0" y1="0" x2="0" y2="1">
        <stop offset="0" stop-color="#0a0a0a"/>
        <stop offset="0.12" stop-color="#150e0f"/>
        <stop offset="0.55" stop-color="#6e2322"/>
        <stop offset="0.9" stop-color="#d92226"/>
        <stop offset="1" stop-color="#e32227"/>
      </linearGradient>
    </defs>

    <g class="pull-streaks">
      <rect x="145" y="258" width="357" height="414" fill="url(#pull-gradient)"/>
      <rect class="pull-gap" x="190" y="258" width="3" height="404"/>
      <rect class="pull-gap" x="236" y="258" width="3" height="404"/>
      <rect class="pull-gap" x="276" y="258" width="3" height="404"/>
      <rect class="pull-gap" x="368" y="258" width="3" height="404"/>
      <rect class="pull-gap" x="412" y="258" width="3" height="404"/>
      <rect class="pull-gap" x="456" y="258" width="3" height="404"/>
    </g>

    <text class="title-word" x="145" y="152" font-size="80" textLength="357" lengthAdjust="spacingAndGlyphs">QUIETER</text>
    <text class="title-connector" x="323" y="188" font-size="28" text-anchor="middle" letter-spacing="22">UNDER</text>
    <text class="title-word" x="145" y="260" font-size="80" textLength="357" lengthAdjust="spacingAndGlyphs">LANTERNS</text>

    <text class="title-word bottom-echo" x="145" y="726" font-size="80" textLength="357" lengthAdjust="spacingAndGlyphs">LANTERNS</text>

    <text class="author-name" x="322" y="629" font-size="12" text-anchor="middle" letter-spacing="0.5">JANE DOE</text>

    <text class="subtitle" x="323" y="752" font-size="16.5" text-anchor="middle">A LEDGER OF HARBOUR SONGS</text>
    <text class="subtitle" x="323" y="776" font-size="16.5" text-anchor="middle">ACROSS MILD WINTERS</text>
  </svg>
</main>
</body>
</html>
```